Marlow Family Chiropractic Stationary

The letterhead and business card must have our logo.
We would like to see the logo used in different ways ( It can be expanded upon in the stationary.)
Please use the the same or similar colors.
Must be eye catching and memorable.
Must be easy to read

Reason: The doctor has been too busy to make any final decisions. He would like to give himself a little more time.

Target Market(s)

Chiropractic Healthcare

Industry/Entity Type

Business

Requirements
Must have
• Dr. Nathaniel Marlow D.C.
Chiropractor

555-555-0193

415 Birchwood Parkway, 2nd Floor
Alderbrook, ZZ 00099

drmarlow@marlowspine.example
www.marlowspine.example
www.facebook.com/MarlowFamilySpine
Should not have
• should not be difficult to read

```html
<!DOCTYPE html>
<html lang="en">
<head>
<meta charset="utf-8">
<title>Marlow Family Chiropractic – Business Card</title>
<link rel="stylesheet" href="https://fonts.googleapis.com/css2?family=PT+Sans:wght@400;700&display=swap">
<style>
  :root {
    --bg: #e9ecee;
    --card-white: #ffffff;
    --brand-green: #3f9a1f;
    --leaf-green: #7dc242;
    --green-light: #a9d86a;
    --green-mid: #6ab42e;
    --leaf-yellow: #d8e06a;
    --ink: #1f1f1f;
    --ink-soft: #3a3a3a;
    --rule: #2a2a2a;
    --brand-dark: #2c5a12;
  }
  * { box-sizing: border-box; margin: 0; padding: 0; }
  html, body { width: 1200px; height: 960px; overflow: hidden; }
  body {
    background: var(--bg);
    font-family: "PT Sans", Arial, sans-serif;
    color: var(--ink);
    display: flex;
    flex-direction: column;
    align-items: center;
    justify-content: center;
    gap: 40px;
  }
  .card {
    width: 760px;
    height: 434px;
    position: relative;
    overflow: hidden;
    box-shadow: 0 6px 22px rgba(0,0,0,0.14);
  }

  /* Front */
  .card--front { background: var(--card-white); padding: 44px 48px; }
  .brand { display: flex; align-items: center; gap: 22px; }
  .brand__mark {
    width: 96px; height: 96px;
    border-radius: 50%;
    background: var(--leaf-green);
    flex: none;
  }
  .brand__name {
    color: var(--brand-green);
    font-weight: 700;
    line-height: 1.05;
    text-transform: uppercase;
  }
  .brand__name .line1 { display: block; font-size: 56px; letter-spacing: 2px; }
  .brand__name .line2 { display: block; font-size: 20px; letter-spacing: 1px; }

  .person { margin-top: 44px; }
  .person__name {
    font-size: 30px;
    font-weight: 400;
    text-transform: uppercase;
    letter-spacing: 0.5px;
  }
  .person__title { font-size: 20px; color: var(--ink-soft); margin-top: 2px; }
  .divider { border: 0; border-top: 2px solid var(--rule); margin: 16px 0 18px; }

  .contact { display: flex; justify-content: space-between; font-size: 19px; }
  .contact__list { list-style: none; display: grid; gap: 6px; }
  .contact__list li { display: flex; align-items: center; gap: 14px; }
  .contact__list li:first-child { font-size: 22px; }
  .icon { width: 20px; height: 20px; flex: none; }
  .icon--square { background: var(--brand-green); }
  .address { font-size: 17px; line-height: 1.35; font-style: normal; text-align: left; }

  /* Back */
  .card--back {
    background: linear-gradient(100deg, var(--green-mid) 0%, var(--leaf-green) 55%, var(--green-light) 100%);
  }
  .back-art {
    position: absolute;
    left: 0; top: 0;
    width: 300px; height: 100%;
    background: radial-gradient(ellipse at 45% 40%, var(--leaf-yellow) 0%, rgba(216,224,106,0.35) 45%, rgba(216,224,106,0) 72%);
  }
  .back-brand {
    position: absolute;
    right: 48px;
    bottom: 52px;
    display: flex;
    align-items: center;
    gap: 20px;
  }
  .back-brand__mark {
    width: 70px; height: 70px;
    border-radius: 50%;
    background: var(--brand-dark);
  }
  .back-brand__name {
    color: var(--brand-dark);
    font-weight: 700;
    text-transform: uppercase;
    text-align: right;
    line-height: 1.05;
  }
  .back-brand__name .line1 { display: block; font-size: 64px; letter-spacing: 4px; }
  .back-brand__name .line2 { display: block; font-size: 24px; letter-spacing: 2px; }
</style>
</head>
<body>

<section class="card card--front" aria-label="Business card front">
  <div class="brand">
    <span class="brand__mark" aria-hidden="true"></span>
    <h1 class="brand__name"><span class="line1">Marlow</span><span class="line2">Family Chiropractic</span></h1>
  </div>

  <div class="person">
    <h2 class="person__name">Dr. Nathaniel Marlow D.C.</h2>
    <p class="person__title">Chiropractor</p>
  </div>
  <hr class="divider">

  <div class="contact">
    <ul class="contact__list">
      <li>
        <svg class="icon" viewBox="0 0 20 20" aria-hidden="true">
          <rect x="4" y="1" width="12" height="18" rx="2" fill="var(--brand-green)"/>
          <rect x="6" y="4" width="8" height="9" fill="#fff"/>
          <circle cx="10" cy="16" r="1.2" fill="#fff"/>
        </svg>
        <span>555-555-0193</span>
      </li>
      <li>
        <svg class="icon" viewBox="0 0 20 20" aria-hidden="true">
          <rect x="1.5" y="4" width="17" height="12" fill="none" stroke="var(--brand-green)" stroke-width="1.8"/>
          <path d="M1.5 4 L10 11 L18.5 4" fill="none" stroke="var(--brand-green)" stroke-width="1.8"/>
        </svg>
        <span>drmarlow@marlowspine.example</span>
      </li>
      <li>
        <span class="icon icon--square" aria-hidden="true"></span>
        <span>/MarlowFamilySpine</span>
      </li>
    </ul>
    <address class="address">
      415 Birchwood Parkway, 2nd Floor<br>
      Alderbrook, ZZ 00099<br>
      www.marlowspine.example
    </address>
  </div>
</section>

<section class="card card--back" aria-label="Business card back">
  <div class="back-art" role="img" aria-label="Large leafy tree illustration with family figures along the left edge"></div>
  <div class="back-brand">
    <span class="back-brand__mark" aria-hidden="true"></span>
    <p class="back-brand__name"><span class="line1">Marlow</span><span class="line2">Family Chiropractic</span></p>
  </div>
</section>

</body>
</html>
```